来年3月31日に期限が迫っているインボイス制度について、まだまだ関係ある方にも周知はされていません。
もちろん税務関係なので、税理士さんを始めとして、いろいろな方が、セミナー開催やポルネットとかでも語っていらっしゃいます。
ところが、職種によっては、今更、込み入った話など聞きたくない、面倒だ、聞いてもよく理解できないといった方が多々おられます。
私は、建築関係の経理に携わっており、身近にも、そんな方々を目にしていて危惧している状態です。
これが全国となったら、いったいどれだけの人が、わからないまま期日を迎えてしまうのでしょう。
その中で、とくに今回 ひとり親方にターゲットを絞って、せめて、その方々に向けて、いちからわかるように、しかも語りかけるつもりで書きました。
本文を添付いたしますので、その意向を汲んでいただいた上での電子書籍の表紙デザインをお願いしたいです。
一目で見て、これなら一度読んでみるかと思っていただけるようなものを期待しております。
是非とも、宜しくお願い致します。

```html
<!DOCTYPE html>
<html lang="ja">
<head>
<meta charset="UTF-8">
<title>ひとり親方のための いちからわかるインボイス制度</title>
<link rel="stylesheet" href="https://fonts.googleapis.com/css2?family=Noto+Sans+JP:wght@500;700;900&display=swap">
<style>
  :root {
    --bg-top: #f4f7fb;
    --bg-bottom: #dfe7f1;
    --navy: #1f2a44;
    --blue: #1a6cc7;
    --blue-dark: #1459a8;
    --orange: #f08a12;
    --red: #e2262e;
    --white: #ffffff;
    --art-light: #e6edf5;
    --art-mid: #c7d3e1;
  }
  * { margin: 0; padding: 0; box-sizing: border-box; }
  html, body { width: 750px; height: 1200px; overflow: hidden; }
  body { font-family: "Noto Sans JP", sans-serif; background: var(--white); }

  .cover {
    position: relative;
    width: 750px;
    height: 1200px;
    overflow: hidden;
    background: linear-gradient(180deg, var(--bg-top) 0%, var(--bg-bottom) 100%);
  }

  .audience-bubble {
    position: absolute;
    left: 28px;
    top: 22px;
    width: 694px;
    height: 96px;
    z-index: 2;
  }
  .audience-bubble svg { position: absolute; inset: 0; }
  .audience-bubble span {
    position: absolute;
    inset: 0 0 12px 0;
    display: flex;
    align-items: center;
    justify-content: center;
    font-weight: 900;
    font-size: 58px;
    color: var(--red);
    letter-spacing: 2px;
  }

  .subtitle {
    position: absolute;
    left: 0;
    width: 100%;
    top: 178px;
    text-align: center;
    font-weight: 900;
    font-size: 96px;
    line-height: 1.2;
    color: var(--navy);
    letter-spacing: 1px;
    z-index: 2;
  }
  .subtitle .accent { color: var(--orange); }

  .spark {
    position: absolute;
    left: 664px;
    top: 190px;
    z-index: 2;
  }

  .title {
    position: absolute;
    left: 0;
    width: 100%;
    top: 296px;
    text-align: center;
    font-weight: 900;
    font-size: 128px;
    line-height: 150px;
    color: var(--blue);
    letter-spacing: 4px;
    z-index: 2;
  }

  .scene-art {
    position: absolute;
    left: 330px;
    top: 600px;
    width: 420px;
    height: 600px;
    background: linear-gradient(180deg, var(--art-light) 0%, var(--art-mid) 100%);
    border-top-left-radius: 40px;
    z-index: 1;
  }

  .author {
    position: absolute;
    left: 62px;
    top: 775px;
    font-weight: 700;
    font-size: 36px;
    color: var(--navy);
    letter-spacing: 4px;
    z-index: 2;
  }
  .author small { font-size: 24px; margin-left: 10px; }

  .pitch-box {
    position: absolute;
    left: 0;
    top: 850px;
    width: 540px;
    height: 350px;
    background: var(--blue-dark);
    border-top-right-radius: 10px;
    padding: 30px 20px 0 36px;
    z-index: 3;
  }
  .pitch-box p {
    font-weight: 900;
    font-size: 52px;
    line-height: 1.32;
    color: var(--white);
    letter-spacing: 1px;
  }
  .pitch-box .target {
    position: absolute;
    left: 22px;
    top: 278px;
    width: 498px;
    height: 48px;
    border-radius: 24px;
    background: var(--white);
    color: var(--navy);
    font-weight: 700;
    font-size: 23px;
    display: flex;
    align-items: center;
    justify-content: center;
  }
</style>
</head>
<body>
  <main class="cover">
    <div class="audience-bubble">
      <svg width="694" height="96" viewBox="0 0 694 96">
        <path d="M40 4 H654 A36 36 0 0 1 690 40 V44 A36 36 0 0 1 654 80 H300 L280 94 L268 80 H40 A36 36 0 0 1 4 44 V40 A36 36 0 0 1 40 4 Z"
              fill="#ffffff" stroke="#e2262e" stroke-width="4"/>
      </svg>
      <span>ひとり親方のための</span>
    </div>

    <h2 class="subtitle">いちから<span class="accent">わかる</span></h2>

    <svg class="spark" width="60" height="60" viewBox="0 0 60 60" aria-hidden="true">
      <g stroke="#f08a12" stroke-width="6" stroke-linecap="round">
        <line x1="10" y1="36" x2="22" y2="26"/>
        <line x1="20" y1="50" x2="40" y2="46"/>
        <line x1="6" y1="16" x2="12" y2="4"/>
      </g>
    </svg>

    <h1 class="title">インボイス<br>制度</h1>

    <div class="scene-art" role="img" aria-label="ビル群を背景に、書類を持ちヘルメットをかぶった作業着の職人のイラスト"></div>

    <p class="author">森川　佳子<small>著</small></p>

    <section class="pitch-box">
      <p>わかりやすく<br>仕組みと取り<br>組みを紹介！</p>
      <div class="target">ひとり親方、その他の個人事業主へ！</div>
    </section>
  </main>
</body>
</html>
```